Business card design for Automotive workshop

We need a business card for a new automotive repair and tyre shop called Ridgeback Prime Automotive located in New Zealand. We are a clean, modern and fresh workshop and company.

Front needs to feature logo,
my name:
Lachie Westergaard (director)

Address:
48 Marlow Lane
Whitianga 3510

Phone: 07 842 1937
Mobile: 027 519 2764
Email: office@ridgebackmotors.co.nz
Website: ridgebackmotors.co.nz

Back needs to feature an area to write down appointment details, date and time.

Also feature a list of jobs and work we do such as,
Vehicle Servicing
All Mechanical Repairs
Warrant of Fitness
Tyres & Wheel Alignments
Automotive Diagnostics
Automotive Parts & Supplies

```html
<!DOCTYPE html>
<html lang="en">
<head>
<meta charset="utf-8">
<title>Ridgeback Prime Automotive — Business Card</title>
<link rel="stylesheet" href="https://fonts.googleapis.com/css2?family=Signika:wght@400;500;600;700&display=swap">
<style>
  :root {
    --red: #e31e26;
    --black: #000000;
    --white: #ffffff;
    --ink: #3b3b3b;
    --field: #efeff1;
    --page: #f0f0f2;
  }
  * { box-sizing: border-box; margin: 0; padding: 0; }
  html, body { width: 1200px; height: 1200px; overflow: hidden; }
  body {
    background: var(--page);
    font-family: "Signika", sans-serif;
    position: relative;
  }
  .card {
    position: absolute;
    left: 240px;
    width: 720px;
    height: 420px;
    overflow: hidden;
    box-shadow: 0 1px 4px rgba(0,0,0,0.18);
  }

  /* Front */
  .card-front { top: 150px; background: var(--black); color: var(--white); }
  .brand-name {
    position: absolute; left: 0; right: 0; top: 128px;
    text-align: center;
    font-weight: 700; font-size: 33px; letter-spacing: 1.5px;
    color: var(--red); text-transform: uppercase;
  }
  .website {
    position: absolute; left: 0; right: 0; top: 206px;
    text-align: center;
    font-size: 18px; letter-spacing: 4.5px; color: var(--red);
  }
  .holder {
    position: absolute; left: 18px; top: 290px;
    font-size: 21px; font-weight: 500;
  }
  .holder .role { font-size: 11px; font-weight: 400; }
  .holder-rule {
    position: absolute; left: 18px; top: 317px; width: 231px; height: 3px;
    background: linear-gradient(to right, var(--red) 0 40%, var(--white) 40% 100%);
  }
  .phone {
    position: absolute; top: 338px;
    display: flex; align-items: center; gap: 8px;
    font-size: 19px; font-weight: 500;
  }
  .phone-mobile { left: 18px; }
  .phone-office { left: 193px; }
  .phone svg { width: 15px; height: 15px; }
  .contact-band { position: absolute; left: 0; top: 377px; width: 720px; height: 44px; }
  .email {
    position: absolute; left: 21px; top: 386px;
    display: flex; align-items: center; gap: 10px;
    font-size: 19px; font-weight: 500; color: var(--white);
  }
  .address {
    position: absolute; right: 32px; top: 392px;
    display: flex; align-items: center; gap: 7px;
    font-size: 18px; font-weight: 600; color: var(--red);
  }

  /* Back */
  .card-back { top: 629px; background: var(--white); }
  .frame { position: absolute; inset: 0; }
  .brand-name-small {
    position: absolute; left: 0; right: 0; top: 50px;
    text-align: center;
    font-weight: 700; font-size: 19px; letter-spacing: 1px;
    color: var(--red); text-transform: uppercase;
  }
  .services { position: absolute; left: 31px; top: 0; list-style: none; }
  .services li {
    position: absolute; left: 0; white-space: nowrap;
    display: flex; align-items: center; gap: 10px;
    font-size: 21px; font-weight: 500; color: var(--ink);
  }
  .services li::before {
    content: ""; width: 11px; height: 11px; border-radius: 50%;
    border: 2.5px solid var(--red); flex: none;
  }
  .appointment { position: absolute; left: 355px; width: 317px; }
  .field {
    position: absolute; left: 0; width: 100%;
    background: var(--field);
    border-radius: 3px 3px 0 0;
    font-size: 14px; color: var(--ink);
    padding: 9px 8px;
  }
  .field-date { top: 113px; height: 36px; border-bottom: 1.5px solid #333; }
  .field-time { top: 158px; height: 36px; border-bottom: 1.5px solid var(--red); }
  .field-details { top: 202px; height: 173px; border-bottom: 1.5px solid var(--red); }
</style>
</head>
<body>

<section class="card card-front" aria-label="Business card front">
  <div class="brand-name">Ridgeback Prime Automotive</div>
  <div class="website">ridgebackmotors.co.nz</div>

  <div class="holder">Lachie Westergaard <span class="role">(director)</span></div>
  <div class="holder-rule"></div>

  <div class="phone phone-mobile">
    <svg viewBox="0 0 24 24" fill="none" stroke="#e31e26" stroke-width="2"><rect x="3" y="9" width="18" height="11" rx="2"/><path d="M3 9c2-5 16-5 18 0M9 13h6M8 16h8"/></svg>
    027 519 2764
  </div>
  <div class="phone phone-office">
    <svg viewBox="0 0 24 24" fill="none" stroke="#e31e26" stroke-width="2"><path d="M5 3h4l2 5-3 2a12 12 0 0 0 6 6l2-3 5 2v4a2 2 0 0 1-2 2A17 17 0 0 1 3 5a2 2 0 0 1 2-2z"/></svg>
    07 842 1937
  </div>

  <svg class="contact-band" viewBox="0 0 720 44" preserveAspectRatio="none">
    <rect x="0" y="9" width="720" height="35" fill="#ffffff"/>
    <polygon points="0,0 375,0 358,44 0,44" fill="#e31e26"/>
  </svg>
  <div class="email">
    <svg width="18" height="14" viewBox="0 0 18 14" fill="none" stroke="#fff" stroke-width="1.6"><rect x="1" y="1" width="16" height="12"/><path d="M1 1l8 7 8-7"/></svg>
    office@ridgebackmotors.co.nz
  </div>
  <div class="address">
    <svg width="14" height="18" viewBox="0 0 14 18" fill="none" stroke="#e31e26" stroke-width="1.8"><path d="M7 17s6-6 6-10A6 6 0 0 0 1 7c0 4 6 10 6 10z"/><circle cx="7" cy="7" r="2"/></svg>
    48 Marlow Lane Whitianga 3510
  </div>
</section>

<section class="card card-back" aria-label="Business card back">
  <svg class="frame" viewBox="0 0 720 420">
    <path d="M0 0 H616 V8 a10 10 0 0 1 -10 10 H33 a12 12 0 0 0 -12 12 V298 a9 9 0 0 1 -9 9 H0 Z" fill="#000"/>
    <path d="M720 112 V420 H104 V412 a12 12 0 0 1 12 -12 H701 V124 a12 12 0 0 1 12 -12 Z" fill="#e31e26"/>
  </svg>

  <div class="brand-name-small">Ridgeback Prime Automotive</div>

  <ul class="services">
    <li style="top:109px">Vehicle Servicing</li>
    <li style="top:157px">All Mechanical Repairs</li>
    <li style="top:209px">Warrant of Fitness</li>
    <li style="top:257px">Tyres &amp; Wheel Alignments</li>
    <li style="top:305px">Automotive Diagnostics</li>
    <li style="top:355px">Automotive Parts &amp; Supplies</li>
  </ul>

  <div class="appointment">
    <div class="field field-date">Date</div>
    <div class="field field-time">Time</div>
    <div class="field field-details">Details</div>
  </div>
</section>

</body>
</html>
```